Law Firm Website

We are looking to update our old, tired and very flat website. We have someone who will code and host the site but we need some design inspiration. The website will consist of no more than 2/3 pages, possibly with pop-ups for information. We already have all the blurb. We would like something distinctive, clean and eye-catching, using the purple and white theme that we already use on our firm stationery. Examples uploaded. Current website URL is www.dunmorewillett.example.

Industry/Entity Type

Law Firm

```html
<!DOCTYPE html>
<html lang="en">
<head>
<meta charset="utf-8">
<title>Dunmore + Willett Solicitors</title>
<link rel="stylesheet" href="https://fonts.googleapis.com/css2?family=Mulish:ital,wght@0,400;0,500;0,800;1,400&display=swap">
<style>
:root{
  --purple:#5c5699;
  --purple-deep:#46408a;
  --ink:#3b3b3b;
  --text:#555;
  --footer:#4a4a4a;
  --footer-text:#e6e6e6;
  --grey-logo:#9a9a9a;
  --rule:#d6d6d6;
}
*{margin:0;padding:0;box-sizing:border-box}
html,body{width:1074px;height:1200px;overflow:hidden}
body{position:relative;font-family:"Mulish",sans-serif;color:var(--text);
  background:linear-gradient(#5c5699 0,#5c5699 307px,#e9e9e9 307px,#fff 450px,#fff 100%)}
.abs{position:absolute}
.header{left:107px;top:0;width:860px;height:96px;background:linear-gradient(#fff,#f1f1f1);border-bottom:6px solid var(--purple)}
.brand{left:117px;top:27px;font-weight:800;font-size:29px;color:#2f3a34;line-height:1;white-space:nowrap}
.brand .plus{color:var(--purple)}
.brand-sub{left:166px;top:61px;font-size:14px;font-weight:800;color:var(--purple)}
.nav{position:absolute;right:101px;top:68px;height:28px;display:flex}
.nav a{position:relative;padding:0 12px;font-size:13.5px;color:#333;text-decoration:none;white-space:nowrap;line-height:16px}
.nav a.active{color:var(--purple)}
.nav a.active::after{content:"";position:absolute;left:-6px;right:-6px;bottom:-12px;height:6px;background:var(--purple-deep)}
.hero-frame{left:106px;top:103px;width:862px;height:354px;background:#fff;border:1px solid #e2e2e2}
.hero-photo{left:112px;top:108px;width:850px;height:344px;
  background:linear-gradient(100deg,#c9b9a0 0%,#6a6460 35%,#3a3f4c 55%,#8f8578 80%,#c8b08a 100%)}
.hero-caption{left:455px;top:211px;width:507px;height:138px}
.hero-caption h1{position:absolute;right:20px;top:12px;text-align:right;font-weight:400;font-size:31px;line-height:38px;color:var(--purple-deep);white-space:nowrap}
.dot{width:12px;height:12px;border-radius:50%;background:var(--purple);top:418px}
.dot.on{background:#fff}
.welcome{left:0;width:1074px;top:486px;text-align:center;font-size:21.5px;font-weight:400;color:var(--purple-deep)}
.intro{left:133px;top:528px;width:808px;text-align:center;font-size:11.7px;line-height:20.6px;color:#444}
.divider{left:116px;top:642px;width:842px;height:1px;background:var(--rule)}
.expertise{left:116px;top:667px;width:412px;height:338px;background:var(--purple);color:#fff}
.expertise h2{position:absolute;left:25px;top:15px;font-weight:400;font-size:21px}
.expertise ul{position:absolute;list-style:none;top:56px}
.expertise li{height:28.6px;font-size:12px;padding-left:19px;position:relative;white-space:nowrap}
.expertise li svg{position:absolute;left:0;top:3px}
.col-a{left:25px}.col-b{left:221px}
.view-all{position:absolute;left:259px;top:302px;font-size:12px;letter-spacing:.3px}
.card{left:546px;width:412px;height:160px;background:linear-gradient(90deg,#ececec 0%,#f6f6f6 70%,#fff 100%)}
.card .portrait{position:absolute;left:16px;top:18px;width:136px;height:124px}
.card h3{position:absolute;left:173px;top:16px;font-weight:400;font-size:20px;color:var(--purple-deep);white-space:nowrap}
.card p{position:absolute;left:173px;top:50px;width:235px;font-size:11.6px;line-height:20.6px;color:#444}
.card .more{position:absolute;left:173px;top:118px;font-size:10.5px;color:var(--purple)}
.footer{left:0;top:1026px;width:1074px;height:174px;background:var(--footer);color:var(--footer-text)}
.footer h4{position:absolute;top:22px;font-weight:400;font-size:16px;color:#fff}
.footer .links{position:absolute;top:56px;list-style:none;font-size:11.8px}
.footer .links li{height:20.6px}
.quote{position:absolute;left:117px;top:54px;width:260px;font-style:italic;font-size:11.8px;line-height:20.6px}
.author{position:absolute;left:117px;top:124px;font-size:10.5px}
.social{position:absolute;left:599px;top:56px;list-style:none;font-size:11.8px}
.social li{height:25px;display:flex;align-items:center;gap:11px}
.social .sq{width:19px;height:19px;background:#2f6fb7}
.foot-brand{position:absolute;left:765px;top:22px;font-weight:800;font-size:25px;color:var(--grey-logo);line-height:1;white-space:nowrap}
.foot-sub{position:absolute;left:814px;top:54px;font-weight:800;font-size:13px;color:var(--grey-logo)}
.legal{position:absolute;left:765px;top:89px;font-size:10.8px;line-height:21px}
.scale{position:absolute;right:7px;bottom:8px;font-size:11px}
</style>
</head>
<body>
<header>
  <div class="abs header"></div>
  <div class="abs brand">Dunmore <span class="plus">+</span> Willett</div>
  <div class="abs brand-sub">Solicitors</div>
  <nav class="nav">
    <a class="active" href="#">Home</a>
    <a href="#">Area of Expertise</a>
    <a href="#">Edwin Dunmore</a>
    <a href="#">Martin Willett</a>
    <a href="#">Contact</a>
  </nav>
</header>

<section>
  <div class="abs hero-frame"></div>
  <div class="abs hero-photo" role="img" aria-label="Photo of a team of solicitors in business suits in an office"></div>
  <svg class="abs hero-caption" width="507" height="138" viewBox="0 0 507 138" aria-hidden="true">
    <polygon points="0,0 507,0 507,138 62,138" fill="#ffffff" fill-opacity=".78"/>
  </svg>
  <div class="abs hero-caption"><h1>Dunmore &amp; Willett Solicitors,<br>For The Service You<br>Deserved</h1></div>
  <span class="abs dot on" style="left:503px"></span>
  <span class="abs dot" style="left:521px"></span>
  <span class="abs dot" style="left:540px"></span>
  <span class="abs dot" style="left:558px"></span>
</section>

<main>
  <h2 class="abs welcome">Welcome to Our Website</h2>
  <p class="abs intro">Aliquam molestie, mi et imperdiet euismod, dui purus auctor tellus, et interdum lacus lectus et ante. Sed accumsan sollicitudin sapien, sit amet adipiscing turpis gravida ac. In congue, neque ac lobortis volutpat, libero mauris varius mi, vitae suscipit ipsum ligula vitae risus. Duis aliquam nibh a dui iaculis viverra id a velit. Vivamus egestas risus in magna varius commodo. Sed semper viverra egestas. Etiam pretium porttitor lectus, vel ornare neque porta volutpat.</p>
  <div class="abs divider"></div>

  <section class="abs expertise">
    <h2>Area of Expertise</h2>
    <ul class="col-a">
      <li><svg width="10" height="9" viewBox="0 0 10 9"><path d="M1 5l3 3 5-7" fill="none" stroke="#fff" stroke-width="2"/></svg>Company Matters</li>
      <li><svg width="10" height="9" viewBox="0 0 10 9"><path d="M1 5l3 3 5-7" fill="none" stroke="#fff" stroke-width="2"/></svg>Commercial Matters</li>
      <li><svg width="10" height="9" viewBox="0 0 10 9"><path d="M1 5l3 3 5-7" fill="none" stroke="#fff" stroke-width="2"/></svg>Commercial Crime</li>
      <li><svg width="10" height="9" viewBox="0 0 10 9"><path d="M1 5l3 3 5-7" fill="none" stroke="#fff" stroke-width="2"/></svg>Litigation /Disputes</li>
      <li><svg width="10" height="9" viewBox="0 0 10 9"><path d="M1 5l3 3 5-7" fill="none" stroke="#fff" stroke-width="2"/></svg>Insolvency</li>
      <li><svg width="10" height="9" viewBox="0 0 10 9"><path d="M1 5l3 3 5-7" fill="none" stroke="#fff" stroke-width="2"/></svg>Residential Conveyancing</li>
      <li><svg width="10" height="9" viewBox="0 0 10 9"><path d="M1 5l3 3 5-7" fill="none" stroke="#fff" stroke-width="2"/></svg>Commercial Conveyancing</li>
      <li><svg width="10" height="9" viewBox="0 0 10 9"><path d="M1 5l3 3 5-7" fill="none" stroke="#fff" stroke-width="2"/></svg>Wills &amp; Probate</li>
    </ul>
    <ul class="col-b">
      <li><svg width="10" height="9" viewBox="0 0 10 9"><path d="M1 5l3 3 5-7" fill="none" stroke="#fff" stroke-width="2"/></svg>Estate Planning</li>
      <li><svg width="10" height="9" viewBox="0 0 10 9"><path d="M1 5l3 3 5-7" fill="none" stroke="#fff" stroke-width="2"/></svg>Powers of Attorney</li>
      <li><svg width="10" height="9" viewBox="0 0 10 9"><path d="M1 5l3 3 5-7" fill="none" stroke="#fff" stroke-width="2"/></svg>Care of the Protection</li>
      <li><svg width="10" height="9" viewBox="0 0 10 9"><path d="M1 5l3 3 5-7" fill="none" stroke="#fff" stroke-width="2"/></svg>Divorce/Family</li>
      <li><svg width="10" height="9" viewBox="0 0 10 9"><path d="M1 5l3 3 5-7" fill="none" stroke="#fff" stroke-width="2"/></svg>Pre-Nuptial Aggrements</li>
      <li><svg width="10" height="9" viewBox="0 0 10 9"><path d="M1 5l3 3 5-7" fill="none" stroke="#fff" stroke-width="2"/></svg>Intellectual Property</li>
      <li><svg width="10" height="9" viewBox="0 0 10 9"><path d="M1 5l3 3 5-7" fill="none" stroke="#fff" stroke-width="2"/></svg>Media Law</li>
    </ul>
    <span class="view-all">VIEW ALL SERVICES ››</span>
  </section>

  <article class="abs card" style="top:667px">
    <div class="portrait" role="img" aria-label="Portrait photo of Edwin Dunmore" style="background:linear-gradient(135deg,#8a8278,#4d4a48 60%,#2f3b52)"></div>
    <h3>About Edwin Dunmore</h3>
    <p>Edwin Dunmore qualified as a solicitor in 1987 and spent many years working with a busy commercial practice in North London.</p>
    <span class="more">READ MORE ››</span>
  </article>
  <article class="abs card" style="top:845px">
    <div class="portrait" role="img" aria-label="Black and white portrait photo of Martin Willett" style="background:linear-gradient(135deg,#6e6e6e,#2a2a2a 55%,#0d0d0d)"></div>
    <h3>About Martin Willett</h3>
    <p>Martin Willett has 40 years experience in the law. He qualified in the City of London where he worked for many years ..</p>
    <span class="more">READ MORE ››</span>
  </article>
</main>

<footer class="abs footer">
  <h4 style="left:117px">Testimonials</h4>
  <svg class="abs" style="left:340px;top:26px" width="30" height="12" viewBox="0 0 30 12" aria-hidden="true">
    <path d="M6 1L1 6l5 5M23 1l5 5-5 5" fill="none" stroke="#fff" stroke-width="1.4"/>
  </svg>
  <svg class="abs" style="left:120px;top:59px" width="18" height="12" viewBox="0 0 18 12" aria-hidden="true">
    <path d="M0 12V7C0 3 2 1 6 0v2C4 3 3 4 3 6h4v6zM10 12V7c0-4 2-6 6-7v2c-2 1-3 2-3 4h4v6z" fill="#d8d8d8"/>
  </svg>
  <p class="quote"><span style="padding-left:31px"></span>Aliquam molestie, mi et imperdiet euis-mod, dui purus auctor tellus, et interdum lacus lectus et ante. Sed accumsan sollicitudin..</p>
  <span class="author">-GLEN HARROW</span>

  <h4 style="left:456px">Company</h4>
  <ul class="links" style="left:456px">
    <li>Home</li><li>Are of Expertise</li><li>Edwin Dunmore</li><li>Martin Willett</li><li>Contact</li>
  </ul>

  <h4 style="left:599px">Connect Us</h4>
  <ul class="social">
    <li><span class="sq"></span>Chatterbook</li>
    <li><span class="sq"></span>Chirper</li>
    <li><span class="sq"></span>ProCircle</li>
  </ul>

  <div class="foot-brand">Dunmore + Willett</div>
  <div class="foot-sub">Solicitors</div>
  <p class="legal">Copyright © 2014. All Right Reserved<br>Legal Notice &nbsp;|&nbsp; Privacy Policy</p>
  <span class="scale">x10</span>
</footer>
</body>
</html>
```